Clean professional design needed for landscape property business

We need a logo for a new lawncare, landscaping , property maintenance business called Meadow Trim.
Our services include lawn mowing, garden maintenance, clean ups and some property maintenance.
We want a double sided business card that is clean and very professional using the colour scheme from our logo which is provided.
the business card should have impact as we will use these to drop into people's letterboxes as a marketing drop.
Initially we want to see what you come up with so there is a very wide scope here to work with.
Updates

Project Deadline Extended
Reason: we feel our original deadline was too short. we have extended to give more time for quality submissions.

Target Market(s)

High end property owners who don't wish to do there own gardneing or property maintenance

Industry/Entity Type

Business

Contact Information for Business Card

Name
Postion/ Title
Phone number
mobile
web address
physical address

services offered

Font styles to use
Sans Serif

Requirements
Must have
• curved edges preferrred
Nice to have
• We like the idea of the logo being embossed or etched into the card so it looks like it is below the surface of the card
Should not have
• No stock images or characters.

```html
<!DOCTYPE html>
<html lang="en">
<head>
<meta charset="utf-8">
<title>Meadow Trim – Business Card</title>
<link rel="stylesheet" href="https://fonts.googleapis.com/css2?family=Lato:wght@400;700;900&display=swap">
<style>
  :root {
    --page-bg: #e9e9e7;
    --card-white: #ffffff;
    --card-shade: #ececec;
    --leaf-green: #8cc63f;
    --leaf-green-soft: rgba(140, 198, 63, .45);
    --leaf-green-deep: #5fa52a;
    --ink-grey: #555a5e;
    --rule-grey: #b9bcbe;
  }
  * { box-sizing: border-box; margin: 0; padding: 0; }
  html, body {
    width: 1200px; height: 1031px; overflow: hidden;
    background: var(--page-bg);
    font-family: "Lato", Arial, sans-serif;
  }
  .card {
    position: absolute; left: 170px; top: 265px;
    width: 860px; height: 500px;
    border-radius: 34px;
    background: radial-gradient(ellipse at 40% 35%, var(--card-white) 45%, var(--card-shade) 100%);
    box-shadow: 0 14px 30px rgba(0,0,0,.18), 0 2px 4px rgba(0,0,0,.1);
    overflow: hidden;
  }
  .grass-art {
    position: absolute; right: 0; bottom: 0;
    width: 440px; height: 240px;
    background:
      radial-gradient(ellipse 100% 100% at 100% 100%,
        var(--leaf-green-deep) 0%,
        var(--leaf-green) 45%,
        var(--leaf-green-soft) 70%,
        rgba(140, 198, 63, 0) 100%);
  }
  .brand {
    position: absolute; left: 80px; top: 170px;
    display: flex; align-items: center; gap: 18px;
  }
  .brand-name {
    font-size: 70px; font-weight: 900; letter-spacing: -3px;
    color: var(--ink-grey); line-height: 1;
  }
  .brand-mark { width: 22px; height: 22px; background: var(--leaf-green); }
  .person { position: absolute; left: 150px; top: 290px; }
  .person-name { font-size: 30px; font-weight: 700; color: var(--leaf-green); }
  .person-role { font-size: 21px; color: var(--ink-grey); margin-top: 2px; }
  .contact {
    position: absolute; left: 560px; top: 62px;
    padding-left: 20px; padding-bottom: 6px;
    border-left: 1px solid var(--rule-grey);
  }
  .contact-icons { display: flex; gap: 8px; margin-bottom: 12px; }
  .contact-icons svg { width: 24px; height: 24px; }
  .contact-list {
    list-style: none; font-size: 19px; color: var(--ink-grey);
    line-height: 1.3; white-space: nowrap;
  }
  .contact-list strong { font-weight: 900; }
</style>
</head>
<body>
  <main class="card">
    <div class="grass-art" role="img" aria-label="Illustration of green grass blades rising from the lower right corner of the card"></div>

    <div class="brand">
      <span class="brand-name">Meadow Trim</span>
      <span class="brand-mark" aria-hidden="true"></span>
    </div>

    <div class="person">
      <p class="person-name">Daniel Hartley</p>
      <p class="person-role">Managing Director</p>
    </div>

    <section class="contact">
      <div class="contact-icons" aria-hidden="true">
        <svg viewBox="0 0 26 26"><circle cx="13" cy="13" r="11.5" fill="none" stroke="var(--leaf-green)" stroke-width="1.5"/><path d="M9 8.5c0 5 3.5 8.5 8.5 8.5l1-2.5-2.5-1-1.2 1.2c-1.6-.8-2.7-1.9-3.5-3.5L12.5 10l-1-2.5z" fill="var(--leaf-green)"/></svg>
        <svg viewBox="0 0 26 26"><circle cx="13" cy="13" r="11.5" fill="var(--leaf-green)"/><rect x="7.5" y="9" width="11" height="8" fill="#fff"/><path d="M7.5 9l5.5 4.5L18.5 9" fill="none" stroke="var(--leaf-green)" stroke-width="1.2"/></svg>
        <svg viewBox="0 0 26 26"><circle cx="13" cy="13" r="11.5" fill="var(--leaf-green)"/><circle cx="13" cy="13" r="6" fill="none" stroke="#fff" stroke-width="1.3"/><path d="M7 13h12M13 7c-3 3.5-3 8.5 0 12M13 7c3 3.5 3 8.5 0 12" fill="none" stroke="#fff" stroke-width="1.1"/></svg>
        <svg viewBox="0 0 26 26"><circle cx="13" cy="13" r="11.5" fill="var(--leaf-green)"/><path d="M13 6.5c-2.6 0-4.5 2-4.5 4.4 0 3.3 4.5 8.6 4.5 8.6s4.5-5.3 4.5-8.6c0-2.4-1.9-4.4-4.5-4.4z" fill="#fff"/><circle cx="13" cy="11" r="1.6" fill="var(--leaf-green)"/></svg>
      </div>
      <ul class="contact-list">
        <li>1.888.555.0142</li>
        <li>dan@meadowtrim.com</li>
        <li>www.<strong>meadowtrim</strong>.com</li>
        <li>5870 Willow Crest Rd Austin</li>
        <li>TX 1234-5678</li>
      </ul>
    </section>
  </main>
</body>
</html>
```